Cleaning service website design

We need a new nice web design(logo will be the same) for a new cleaning service Company:

Informations about Company and logo you can take from flyers in attachments.

This is a cleaning service Company which have simple rules and we would like to show that(in checklist form) on website:

- What we do and that we're Cleaning Green

- Why us?

- How much(our pricing is simple)

Also we would like to communicate with clients by some nice/big pictures on website and the most important thing is our phone number and short/fast Freestimate.

Also there should be some space for description about our Company.

Generally all information on main page can be short: about us, about service(what we do), last reviews, tips (for example: Tip of the week) and other can be some introduction to subpage where will be more information.

There will be few subpages like: About us, About our service, Photos(Before and after), Reviews , Tips, FAQ, Contact, Looking for a Job? - most of them will be just text so you can project just one example.

```html
<!DOCTYPE html>
<html lang="en">
<head>
<meta charset="utf-8">
<title>Tidy Nest House Cleaning</title>
<link href="https://fonts.googleapis.com/css2?family=Lobster+Two:ital,wght@0,700;1,700&family=Merriweather:wght@700;900&family=Open+Sans:wght@400;600;700;800&display=swap" rel="stylesheet">
<style>
:root{
  --blue:#1f63b8;
  --blue-dark:#164d94;
  --blue-light:#dbe8f7;
  --green:#8cc63f;
  --green-dark:#6aa22a;
  --ink:#2d2d2d;
  --white:#ffffff;
  --photo-a:#cfe3f2;
  --photo-b:#9fc8e6;
}
*{box-sizing:border-box;margin:0;padding:0}
html,body{width:791px;height:1200px;overflow:hidden;background:var(--white)}
body{position:relative;font-family:"Open Sans",Arial,sans-serif;color:var(--ink)}
.abs{position:absolute}

/* header */
.brand{left:10px;top:6px;display:flex;align-items:center;gap:6px;font-weight:800;font-size:20px;color:var(--blue)}
.brand-dot{width:18px;height:18px;border-radius:50%;background:var(--green)}
.top-phone{right:14px;top:4px;display:flex;align-items:center;gap:6px;font-weight:800;font-size:26px;color:var(--blue)}
.nav{left:153px;top:38px;width:638px;height:30px;background:var(--blue);display:flex;align-items:center;gap:26px;padding-left:20px;font-weight:700;font-size:13px;color:var(--white);white-space:nowrap}

/* sidebar */
.estimate{left:0;top:80px;width:145px;height:592px;background:var(--green);padding:8px}
.side-title{font-weight:800;font-size:15px;color:var(--white);white-space:nowrap;margin-bottom:10px}
.field{height:22px;background:var(--white);border:1px solid var(--green-dark);margin-bottom:13px;font-size:10px;color:#888;padding:3px 5px}
.field.mid{height:42px}
.field.tall{height:84px}
.submit{display:inline-block;margin-top:4px;background:var(--green-dark);color:var(--white);font-size:11px;font-weight:700;padding:3px 12px;border:1px solid var(--white)}
.tip{left:0;top:680px;width:145px;height:480px;background:var(--green);padding:8px}
.tip-photo{width:129px;height:122px;background:linear-gradient(160deg,var(--photo-a),var(--photo-b));margin-bottom:8px}
.tip p{font-size:9.5px;line-height:1.35;color:var(--white);margin-bottom:8px}

/* hero */
.hero-photo{left:153px;top:74px;width:285px;height:498px;background:linear-gradient(180deg,#f3f3f3,#dcdcdc 70%,var(--photo-b))}
.headline{left:390px;top:80px;font-family:"Lobster Two",Georgia,serif;color:var(--blue)}
.headline .l1{font-size:50px;line-height:1;font-style:italic}
.headline .l2{font-size:28px;color:var(--green-dark);margin-left:110px;font-style:italic}
.headline .l3{font-size:58px;line-height:.95;margin-left:150px;font-style:italic}
.h-section{font-family:"Merriweather",Georgia,serif;font-weight:900;font-size:25px;color:var(--ink)}
.checks{list-style:none;font-size:13px;line-height:1.4}
.checks li{display:flex;align-items:flex-start;gap:6px}
.checks svg{flex:none;margin-top:3px}
.why{left:470px;top:232px}
.what{left:470px;top:410px}

/* blue section */
.band{left:153px;top:560px;width:638px;height:540px}
.about{left:172px;top:624px;width:330px;color:var(--white)}
.about h2,.testi h2{font-weight:800;font-size:26px;line-height:1.3}
.about .tag{font-style:italic;font-size:14px;margin-bottom:10px}
.about p{font-size:11px;line-height:1.45;margin-bottom:10px}
.more{display:inline-block;background:var(--green);color:var(--white);font-size:10px;font-weight:700;padding:3px 10px;border-radius:3px}
.testi{left:172px;top:808px;width:330px;color:var(--white)}
.testi h2{margin-bottom:10px}
.quote{font-size:10.5px;line-height:1.45;margin-bottom:6px}
.by{font-size:10.5px;font-weight:700;margin-bottom:14px}

/* pricing */
.socials{left:626px;top:590px;display:flex;gap:6px}
.socials span{width:18px;height:18px;border-radius:50%;background:var(--white)}
.price-card{left:528px;top:614px;width:252px;height:470px;background:var(--white);border-radius:6px;padding:12px 14px;text-align:center}
.pc-title{font-weight:800;font-size:18px;color:var(--blue);text-align:left}
.pc-low{display:flex;align-items:baseline;justify-content:flex-end;gap:6px;font-size:13px;font-style:italic}
.pc-low b{font-size:38px;font-style:normal;color:var(--white);background:var(--green);padding:0 10px;border-radius:4px;line-height:1.1}
.pc-note{font-size:9px;color:var(--green-dark);margin-top:4px}
.links{display:flex;justify-content:space-around;margin:6px 0;height:34px}
.call{border:2px solid var(--blue);border-radius:8px;padding:6px}
.call .c1{font-weight:800;font-size:20px}
.call .c2{display:flex;align-items:center;justify-content:center;gap:6px;font-weight:800;font-size:27px;color:var(--blue)}
.rates{margin-top:10px}
.rate{background:var(--blue);color:var(--white);font-size:12px;font-weight:700;padding:6px;margin-bottom:10px;border-radius:3px}
.large{font-size:11px;color:var(--blue);line-height:1.35}
.large em{display:block;color:var(--green-dark);font-size:10px;margin-top:6px}

/* bottom */
.callout{left:153px;top:1100px;width:638px;height:58px;background:var(--blue);display:flex;align-items:center;justify-content:center;color:var(--blue-light);font-size:16.5px;white-space:nowrap}
.callout b{font-weight:700;color:var(--white);margin-right:5px}
.footer{left:153px;top:1163px;width:638px;height:37px;display:flex;align-items:center;justify-content:space-between;padding:0 14px;font-size:9px;border-top:2px solid var(--blue);white-space:nowrap}
.footer nav{display:flex;gap:8px;font-weight:700;color:var(--blue)}
</style>
</head>
<body>

<header>
  <div class="abs brand"><span class="brand-dot"></span>Tidy Nest</div>
  <div class="abs top-phone">
    <svg width="22" height="22" viewBox="0 0 24 24"><circle cx="12" cy="12" r="11" fill="none" stroke="#1f63b8" stroke-width="2"/><path d="M8 6l2 3-1.5 1.5a8 8 0 0 0 5 5L15 14l3 2-1 2.5c-5 0-10-5-10-10z" fill="#1f63b8"/></svg>
    555-014-2276
  </div>
  <nav class="abs nav"><span>About us</span><span>Services</span><span>Photos</span><span>Reviews</span><span>Tips</span><span>FAQ</span><span>Contact</span><span>Looking for a Job?</span></nav>
</header>

<aside class="abs estimate">
  <div class="side-title">FREE ESTIMATE</div>
  <div class="field">full name</div>
  <div class="field">complete address</div>
  <div class="field">city</div>
  <div class="field">state/province</div>
  <div class="field">zip/postal code</div>
  <div class="field">phone</div>
  <div class="field">email</div>
  <div class="field mid">how did you hear about us?</div>
  <div class="field tall">comments</div>
  <span class="submit">submit</span>
</aside>

<aside class="abs tip">
  <div class="side-title">TIP OF THE WEEK</div>
  <div class="tip-photo" role="img" aria-label="Photo of a cleaner holding spray bottles and cloths"></div>
  <p>Keep a small caddy with your basic supplies in each bathroom. A quick wipe of sinks and mirrors every morning takes two minutes and stops grime from building up, so deep cleans stay short and easy all week.</p>
  <p>Rinse microfiber cloths in warm water after use and let them dry flat. Skip fabric softener, which clogs the fibres and leaves streaks on glass.</p>
</aside>

<section>
  <div class="abs hero-photo" role="img" aria-label="Photo of a smiling cleaner in pink gloves holding a vacuum and a bucket"></div>
  <div class="abs headline">
    <div class="l1">Affordably</div>
    <div class="l2">making your life</div>
    <div class="l3">Simpler</div>
  </div>

  <div class="abs why">
    <h3 class="h-section">Why choose us?</h3>
    <ul class="checks">
      <li><svg width="11" height="11" viewBox="0 0 12 12"><path d="M1 6l3 4 7-9" fill="none" stroke="#6aa22a" stroke-width="2.4"/></svg>Owners Present at Every Cleaning</li>
      <li><svg width="11" height="11" viewBox="0 0 12 12"><path d="M1 6l3 4 7-9" fill="none" stroke="#6aa22a" stroke-width="2.4"/></svg>Locally Owned &amp; Operated</li>
      <li><svg width="11" height="11" viewBox="0 0 12 12"><path d="M1 6l3 4 7-9" fill="none" stroke="#6aa22a" stroke-width="2.4"/></svg>Reliable &amp; Affordable</li>
      <li><svg width="11" height="11" viewBox="0 0 12 12"><path d="M1 6l3 4 7-9" fill="none" stroke="#6aa22a" stroke-width="2.4"/></svg>All Supplies Provided</li>
      <li><svg width="11" height="11" viewBox="0 0 12 12"><path d="M1 6l3 4 7-9" fill="none" stroke="#6aa22a" stroke-width="2.4"/></svg>Green Cleaning</li>
      <li><svg width="11" height="11" viewBox="0 0 12 12"><path d="M1 6l3 4 7-9" fill="none" stroke="#6aa22a" stroke-width="2.4"/></svg>Pet Friendly</li>
      <li><svg width="11" height="11" viewBox="0 0 12 12"><path d="M1 6l3 4 7-9" fill="none" stroke="#6aa22a" stroke-width="2.4"/></svg>No Contracts</li>
    </ul>
  </div>

  <div class="abs what">
    <h3 class="h-section">What do we do?</h3>
    <ul class="checks">
      <li><svg width="11" height="11" viewBox="0 0 12 12"><path d="M1 6l3 4 7-9" fill="none" stroke="#6aa22a" stroke-width="2.4"/></svg>Thoroughly clean your bathrooms,<br>kitchen, bedrooms and living areas</li>
      <li><svg width="11" height="11" viewBox="0 0 12 12"><path d="M1 6l3 4 7-9" fill="none" stroke="#6aa22a" stroke-width="2.4"/></svg>Mop or vacuum your floors</li>
      <li><svg width="11" height="11" viewBox="0 0 12 12"><path d="M1 6l3 4 7-9" fill="none" stroke="#6aa22a" stroke-width="2.4"/></svg>Dust surfaces</li>
      <li><svg width="11" height="11" viewBox="0 0 12 12"><path d="M1 6l3 4 7-9" fill="none" stroke="#6aa22a" stroke-width="2.4"/></svg>Collect garbage</li>
      <li><svg width="11" height="11" viewBox="0 0 12 12"><path d="M1 6l3 4 7-9" fill="none" stroke="#6aa22a" stroke-width="2.4"/></svg>Make beds</li>
    </ul>
  </div>
</section>

<svg class="abs band" viewBox="0 0 638 540" preserveAspectRatio="none" aria-hidden="true">
  <path d="M0 40 Q160 0 320 20 T638 12 V540 H0z" fill="#1f63b8"/>
</svg>

<section>
  <div class="abs about">
    <h2>ABOUT US</h2>
    <div class="tag">It's about caring, not just cleaning.</div>
    <p>Having personally experienced the struggles of finding quality maid service for our home, we want to make it simpler for families in the region. Our goal is to provide caring, consistent and reliable house cleaning to every customer we serve.</p>
    <span class="more">learn more »</span>
  </div>
  <div class="abs testi">
    <h2>TESTIMONIALS</h2>
    <p class="quote">"The service is great, they left my house very clean, no evidence of dirt, my bathroom looks new and my kids are happy. They really did a great job on what they did."</p>
    <p class="by">by: Dana Whitfield</p>
    <p class="quote">"The service is great, they left my house very clean, no evidence of dirt, my bathroom looks new and my kids are happy. They really did a great job on what they did."</p>
    <p class="by">by: Dana Whitfield</p>
  </div>

  <div class="abs socials" aria-hidden="true"><span></span><span></span><span></span><span></span><span></span></div>

  <div class="abs price-card">
    <div class="pc-title">HOUSE CLEANING</div>
    <div class="pc-low">as low as <b>$79.00</b></div>
    <div class="pc-note">*rates are for regular service* &nbsp;PROMPT WEEKEND</div>
    <div class="links" aria-hidden="true">
      <svg width="12" height="34" viewBox="0 0 12 34"><circle cx="6" cy="5" r="3.5" fill="none" stroke="#1f63b8" stroke-width="2"/><line x1="6" y1="9" x2="6" y2="25" stroke="#1f63b8" stroke-width="2.5"/><circle cx="6" cy="29" r="3.5" fill="none" stroke="#1f63b8" stroke-width="2"/></svg>
      <svg width="12" height="34" viewBox="0 0 12 34"><circle cx="6" cy="5" r="3.5" fill="none" stroke="#1f63b8" stroke-width="2"/><line x1="6" y1="9" x2="6" y2="25" stroke="#1f63b8" stroke-width="2.5"/><circle cx="6" cy="29" r="3.5" fill="none" stroke="#1f63b8" stroke-width="2"/></svg>
    </div>
    <div class="call">
      <div class="c1">CALL NOW!</div>
      <div class="c2">
        <svg width="24" height="24" viewBox="0 0 24 24"><circle cx="12" cy="12" r="11" fill="none" stroke="#1f63b8" stroke-width="2"/><path d="M8 6l2 3-1.5 1.5a8 8 0 0 0 5 5L15 14l3 2-1 2.5c-5 0-10-5-10-10z" fill="#1f63b8"/></svg>
        555-014-2276
      </div>
    </div>
    <div class="links" aria-hidden="true">
      <svg width="12" height="34" viewBox="0 0 12 34"><circle cx="6" cy="5" r="3.5" fill="none" stroke="#1f63b8" stroke-width="2"/><line x1="6" y1="9" x2="6" y2="25" stroke="#1f63b8" stroke-width="2.5"/><circle cx="6" cy="29" r="3.5" fill="none" stroke="#1f63b8" stroke-width="2"/></svg>
      <svg width="12" height="34" viewBox="0 0 12 34"><circle cx="6" cy="5" r="3.5" fill="none" stroke="#1f63b8" stroke-width="2"/><line x1="6" y1="9" x2="6" y2="25" stroke="#1f63b8" stroke-width="2.5"/><circle cx="6" cy="29" r="3.5" fill="none" stroke="#1f63b8" stroke-width="2"/></svg>
    </div>
    <div class="rates">
      <div class="rate">$79 for homes less than 1000 sq.ft</div>
      <div class="rate">$89 for homes 1000-1800 sq.ft</div>
      <div class="rate">$99 for homes 1800-2800 sq.ft</div>
    </div>
    <div class="large">*If your home is larger than 2800 sq.ft please call for a quote<em>*rates are for regular service*</em></div>
  </div>
</section>

<div class="abs callout"><b>CALL 555-014-2276</b> or fill out the form to the right to simplify your life!</div>

<footer class="abs footer">
  <nav><span>About us</span><span>Services</span><span>Photos</span><span>Reviews</span><span>Tips</span><span>FAQ</span><span>Contact</span><span>Looking for a Job?</span></nav>
  <span>© 2013 Tidy Nest House Cleaning. All rights reserved.</span>
</footer>

</body>
</html>
```